Flyer Design Project

Family owned and operated roof repair, cleaning and restoration business. Offering quality service and product at a quality price. Have been in existence for over 25 years.
I have just had a logo designed for the business. I would like to generate business by getting people to look at their roof and consider the maintenance and appearance.
Must generate a serious approach as there have been some operators who have acted poorly.
We DO NOT pressure sell, but gladly provide quotes and advice. We only use the best quality products and we are a licensed applicator of this product.
Our finished product will protect homes and increase their value.
Target Market(s)
Home owners who have a house with concrete roof tiles.
Industry/Entity Type
Business
Look and feel

```html
<!DOCTYPE html>
<html lang="en">
<head>
<meta charset="utf-8">
<title>Trueline Roof Restoration Flyer</title>
<link href="https://fonts.googleapis.com/css2?family=Cinzel:wght@400;600&family=PT+Sans:wght@400&family=Questrial&display=swap" rel="stylesheet">
<style>
  :root {
    --ink: #0c0c0c;
    --brand-blue: #2f6f93;
    --heading-blue: #1f6488;
    --rule-blue: #9fcde6;
    --paper: #f5f5f5;
    --text: #222222;
    --box-grey: #bdbdbd;
    --white: #ffffff;
    --footer-text: #e6e6e6;
  }
  * { margin: 0; padding: 0; box-sizing: border-box; }
  html, body { width: 930px; height: 1200px; overflow: hidden; background: var(--paper); }
  .flyer { position: relative; width: 930px; height: 1200px; overflow: hidden; background: var(--paper); font-family: "PT Sans", sans-serif; color: var(--text); }

  .hero { position: absolute; left: 0; top: 0; width: 930px; height: 490px; }
  .hero svg { display: block; }

  .logo-tab {
    position: absolute; left: 306px; top: 0; width: 345px; height: 173px;
    background: var(--ink); border-radius: 0 0 40px 40px;
    display: flex; align-items: center; justify-content: center;
  }
  .logo-tab::before {
    content: ""; position: absolute; inset: 0 8px 8px 8px;
    border: 2px dashed #d9d9d9; border-top: none; border-radius: 0 0 34px 34px;
  }
  .brand-name { font-family: "Cinzel", serif; font-weight: 600; color: var(--white); font-size: 30px; text-align: center; line-height: 1.15; }
  .brand-name .brand-sub { display: block; font-size: 19px; }

  .headline {
    position: absolute; left: 0; top: 432px; width: 930px; text-align: center;
    font-family: "Cinzel", serif; font-weight: 600; font-size: 39px; line-height: 46px; color: var(--ink); letter-spacing: .5px;
  }
  .divider { position: absolute; left: 62px; top: 544px; width: 805px; height: 2px; background: var(--rule-blue); }

  .photo { position: absolute; }
  .photo-house { left: 60px; top: 555px; width: 181px; height: 152px; background: radial-gradient(circle at 50% 45%, #d9b36a 0%, #c79a5a 35%, #f0e6d8 70%, #ffffff 100%); }

  .section { position: absolute; }
  .section h2 { font-family: "Cinzel", serif; font-weight: 400; font-size: 22px; color: var(--heading-blue); line-height: 24px; letter-spacing: .3px; margin-bottom: 1px; }
  .section p { font-size: 15px; line-height: 21px; }
  .section-one { left: 301px; top: 573px; width: 560px; }
  .section-two { left: 61px; top: 738px; width: 805px; }
  .section-three { left: 52px; top: 878px; width: 562px; }

  .offer-box {
    position: absolute; left: 620px; top: 846px; width: 266px; height: 175px;
    border: 5px solid var(--box-grey); border-radius: 30px; text-align: center;
    font-family: "Cinzel", serif; color: var(--heading-blue);
  }
  .offer-box h3 { font-weight: 400; font-size: 16px; line-height: 20px; margin-top: 25px; margin-bottom: 18px; }
  .offer-box ul { list-style: none; }
  .offer-box li { font-size: 16.5px; line-height: 21px; }

  .footer { position: absolute; left: 0; top: 1061px; width: 930px; height: 139px; background: var(--ink); color: var(--white); }
  .footer-brand { position: absolute; left: 56px; top: 40px; }
  .footer-brand .brand-name { text-align: left; }
  .footer-title { position: absolute; left: 408px; top: 22px; font-family: "Cinzel", serif; font-size: 28px; line-height: 36px; letter-spacing: .5px; white-space: nowrap; }
  .footer-contacts { position: absolute; left: 402px; top: 76px; font-family: "Questrial", sans-serif; font-size: 12.5px; line-height: 18px; color: var(--footer-text); }
  .footer-contacts div { position: absolute; top: 0; white-space: nowrap; }
  .contact-address { left: 0; }
  .contact-box { left: 206px; }
  .contact-phone { left: 348px; }
</style>
</head>
<body>
<div class="flyer">
  <div class="hero">
    <svg width="930" height="490" viewBox="0 0 930 490">
      <defs>
        <linearGradient id="heroScene" x1="0" y1="0" x2="0" y2="1">
          <stop offset="0" stop-color="#6ea7dc"/>
          <stop offset="0.35" stop-color="#bcd8ee"/>
          <stop offset="0.6" stop-color="#7fae4c"/>
          <stop offset="1" stop-color="#9fcf4a"/>
        </linearGradient>
      </defs>
      <rect width="930" height="490" fill="url(#heroScene)" role="img" aria-label="Photo of a yellow two-storey house on a green lawn under a blue sky, with a roofer in a hard hat kneeling and holding a power drill"/>
      <path d="M0,418 Q430,320 930,432 L930,490 L0,490 Z" fill="var(--ink)"/>
      <path d="M0,428 Q430,340 930,462 L930,490 L0,490 Z" fill="var(--brand-blue)"/>
      <path d="M0,438 Q430,356 930,476 L930,490 L0,490 Z" fill="var(--paper)"/>
    </svg>
  </div>

  <div class="logo-tab">
    <div class="brand-name">TRUELINE<span class="brand-sub">Roof Restoration</span></div>
  </div>

  <h1 class="headline">Trueline Roof Restoration IS<br>THE BEST FOR YOU!</h1>
  <div class="divider"></div>

  <div class="photo photo-house" role="img" aria-label="Photo of a hand holding a small model house"></div>

  <section class="section section-one">
    <h2>Lorem Ipsum este pur</h2>
    <p>Family owned and operated roof repair, cleaning and restoration business. Offering quality service and product at a quality price. Have been in existence for over 25 years. Family owned and operated roof repair, cleaning and restoration business. Offering quality service and product at a quality price. Have been in existence for over 25 years.</p>
  </section>

  <section class="section section-two">
    <h2>Lorem Ipsum este pur</h2>
    <p>Family owned and operated roof repair, cleaning and restoration business. Offering quality service and product at a quality price. Have been in existence for over 25 years. Family owned and operated roof repair, cleaning and restoration business.</p>
  </section>

  <section class="section section-three">
    <h2>Lorem Ipsum este pur</h2>
    <p>Family owned and operated roof repair, cleaning and restoration business. Offering quality service and product at a quality price. Have been in existence for over 25 years. Family owned and operated roof repair, cleaning and restoration business.</p>
  </section>

  <aside class="offer-box">
    <h3>We offer:</h3>
    <ul>
      <li>Forclosure Clean-Up</li>
      <li>Commercial Clean-Up</li>
      <li>Janitorial Clean-Up</li>
      <li>Maid Service</li>
    </ul>
  </aside>

  <footer class="footer">
    <div class="footer-brand">
      <div class="brand-name">TRUELINE<span class="brand-sub">Roof Restoration</span></div>
    </div>
    <div class="footer-title">Trueline Roof Restoration</div>
    <div class="footer-contacts">
      <div class="contact-address">Unit 18, Harbour Lane, 2nd Floor<br>Westmere</div>
      <div class="contact-box">P.O. Box 4402871<br>WM</div>
      <div class="contact-phone">Tel: +987 65 432 1098<br>Fax: +987 65 432 1099</div>
    </div>
  </footer>
</div>
</body>
</html>
```